Wren's Home Care Business Card

Business card design
Font must be in Poppins Regular for Wren's Home Care
Kind Hands Every Day font is Alex Brush

Colour must be Hex #910E2B
RGB 145-14-43
Pantone 7427 C
We want the card editable
On the front please include
Name eg Marla Dunstow
Position eg Clinical Care Manager
Phone number mobile 0473 586 342
Phone 08 7394 2606
Email : marla@wrenshomecare-demo.com.au
Address : Quiet Cove, Southern Shire, 4821
Website : wrenshomecare-demo.com.au
Contact us today to experience the warmth, respect and personal touch of Wren's Home Care.

Target Market(s)

35+

Industry/Entity Type

aged care / community

Contact Information for Business Card

see project description

Requirements
Must have
• Colours, logos and fonts as detailed and uploaded

```html
<!DOCTYPE html>
<html lang="en">
<head>
<meta charset="utf-8">
<title>Wren's Home Care – Business Card</title>
<link href="https://fonts.googleapis.com/css2?family=Alex+Brush&family=Poppins:wght@400;600;700&display=swap" rel="stylesheet">
<style>
  :root {
    --brand: #910E2B;
    --brand-faint: #efdfe2;
    --card: #ffffff;
    --card-shade: #ececec;
    --stage: #2b2b2d;
    --ink-soft: #555555;
  }
  * { box-sizing: border-box; margin: 0; padding: 0; }
  html, body { width: 1200px; height: 900px; overflow: hidden; }
  body {
    background: var(--stage);
    font-family: "Poppins", sans-serif;
    color: var(--brand);
    position: relative;
  }
  .card {
    position: absolute;
    width: 700px;
    height: 400px;
    background: linear-gradient(120deg, var(--card-shade) 0%, var(--card) 55%, var(--card) 100%);
    overflow: hidden;
    box-shadow: 0 10px 30px rgba(0,0,0,.45);
  }
  .card--back { left: 110px; top: 45px; }
  .card--front { left: 390px; top: 465px; }

  .faint-ring {
    position: absolute;
    width: 250px; height: 250px;
    border: 14px solid var(--brand-faint);
    border-radius: 50%;
  }
  .card--back .faint-ring { right: 40px; top: 80px; }
  .card--front .faint-ring { right: 30px; top: 140px; }

  .back-message {
    position: absolute;
    left: 44px; top: 60px;
    font-size: 17px;
    line-height: 1.45;
    width: 390px;
  }
  .back-message strong { font-weight: 700; display: block; }

  .brand {
    position: absolute;
    right: 44px; top: 30px;
    display: flex; align-items: center; gap: 14px;
  }
  .brand-mark {
    width: 70px; height: 70px;
    border: 6px solid var(--brand);
    border-radius: 50%;
    flex: none;
  }
  .brand-text { display: flex; flex-direction: column; }
  .brand-name {
    font-weight: 400;
    font-size: 30px;
    line-height: 1.05;
  }
  .brand-tagline {
    font-family: "Alex Brush", cursive;
    font-size: 24px;
    line-height: 1.1;
    margin-top: 4px;
  }

  .rule {
    position: absolute;
    left: 300px; right: 40px; top: 130px;
    height: 1px;
    background: var(--brand);
    opacity: .7;
  }

  .person {
    position: absolute;
    left: 44px; top: 160px;
  }
  .person-name {
    font-weight: 700;
    font-size: 20px;
    letter-spacing: .3px;
    text-transform: uppercase;
  }
  .person-role {
    font-size: 15px;
    color: var(--ink-soft);
    margin-top: -2px;
  }

  .contacts {
    position: absolute;
    left: 44px; top: 235px;
    list-style: none;
    font-size: 14.5px;
    color: var(--ink-soft);
  }
  .contacts li {
    display: flex; align-items: center; gap: 12px;
    height: 27px;
  }
  .contacts svg { width: 16px; height: 16px; flex: none; }
</style>
</head>
<body>

  <section class="card card--back" aria-label="Card back">
    <div class="faint-ring" aria-hidden="true"></div>
    <p class="back-message">Contact us today to experience the warmth, respect and personal touch of <strong>Wren's Home Care.</strong></p>
  </section>

  <section class="card card--front" aria-label="Card front">
    <div class="faint-ring" aria-hidden="true"></div>

    <div class="brand">
      <div class="brand-mark" aria-hidden="true"></div>
      <div class="brand-text">
        <span class="brand-name">Wren's<br>Home Care</span>
        <span class="brand-tagline">Kind Hands Every Day</span>
      </div>
    </div>

    <div class="rule" aria-hidden="true"></div>

    <div class="person">
      <h1 class="person-name">Marla Dunstow</h1>
      <p class="person-role">Clinical Care Manager</p>
    </div>

    <ul class="contacts">
      <li>
        <svg viewBox="0 0 16 16" aria-hidden="true"><rect x="4" y="1" width="8" height="14" rx="1.5" fill="none" stroke="#910E2B" stroke-width="1.6"/><line x1="7" y1="12.5" x2="9" y2="12.5" stroke="#910E2B" stroke-width="1.4"/></svg>
        0473 586 342
      </li>
      <li>
        <svg viewBox="0 0 16 16" aria-hidden="true"><path d="M3 1.5l3 .5 1 3-2 1.3a8 8 0 0 0 4.7 4.7L10 9l3 1 .5 3-2 1.5C6 14 1.5 9.5 1.5 3.5z" fill="#910E2B"/></svg>
        08 7394 2606
      </li>
      <li>
        <svg viewBox="0 0 16 16" aria-hidden="true"><rect x="1" y="3" width="14" height="10" fill="#910E2B"/><path d="M1 3l7 5.5L15 3" fill="none" stroke="#fff" stroke-width="1.3"/></svg>
        marla@wrenshomecare-demo.com.au
      </li>
      <li>
        <svg viewBox="0 0 16 16" aria-hidden="true"><g fill="none" stroke="#910E2B" stroke-width="1.2"><circle cx="8" cy="8" r="6.5"/><ellipse cx="8" cy="8" rx="3" ry="6.5"/><line x1="1.5" y1="8" x2="14.5" y2="8"/><line x1="2.5" y1="4.5" x2="13.5" y2="4.5"/><line x1="2.5" y1="11.5" x2="13.5" y2="11.5"/></g></svg>
        wrenshomecare-demo.com.au
      </li>
      <li>
        <svg viewBox="0 0 16 16" aria-hidden="true"><path d="M8 15s-5-5.2-5-8.5a5 5 0 0 1 10 0C13 9.8 8 15 8 15z" fill="#910E2B"/><circle cx="8" cy="6.5" r="1.8" fill="#fff"/></svg>
        Quiet Cove, Southern Shire, 4821
      </li>
    </ul>
  </section>

</body>
</html>
```